looking for sleek business card to standout from the crowd!

We are a young biotechnology company looking to help you personalize your health through understanding your genetic make up. We need you help in making a clean but sleek business card design using our new logo. The goal? Any time we give our cards out, people say "nice card!" The feel we are going for is "modern-techy". We don't want to come across as an old, giant pharma company, but not trying to be a hipster either.

Target Market(s)

healthcare and biotechnology industry.

Industry/Entity Type

Biotechnology

Contact Information for Business Card

Info to include on the card will be NAME, TITLE, EMAIL, PHONE. The companies website (www.corvalinbio.com) should also be on the card some where. Would like the logo, when printed, to be raised.

Requirements
Must have
• The logo we have attached in the color it is in. Fonts for text should lean toward more professional/tech.
Nice to have
• Prefer white/light color background
Should not have
• cartoons, landscape backgrounds images.

```html
<!DOCTYPE html>
<html lang="en">
<head>
<meta charset="utf-8">
<title>Corvalin Business Card</title>
<link rel="stylesheet" href="https://fonts.googleapis.com/css2?family=Lato:wght@400;700;900&display=swap">
<style>
  :root {
    --stage: #3a3d42;
    --card-dark: #262628;
    --light-tint: #e4e4e4;
    --brand-blue: #1a78c2;
    --brand-blue-soft: #3d92d4;
    --brand-green: #7cc242;
    --ink-grey: #555a60;
    --ink-white: #ffffff;
    --ink-soft: #d8d8d8;
  }
  * { margin: 0; padding: 0; box-sizing: border-box; }
  html, body {
    width: 1200px;
    height: 900px;
    overflow: hidden;
    background: var(--stage);
    font-family: "Lato", sans-serif;
  }
  .stage {
    width: 1200px;
    height: 900px;
    display: flex;
    flex-direction: column;
    align-items: center;
    justify-content: center;
    gap: 60px;
  }
  .card {
    width: 560px;
    height: 320px;
    display: block;
    box-shadow: 0 14px 30px rgba(0,0,0,0.35);
  }
  .brand-name {
    font-family: "Lato", sans-serif;
    font-weight: 900;
    fill: var(--brand-blue);
    letter-spacing: 2px;
  }
  .site-line {
    font-family: "Lato", sans-serif;
    font-size: 15px;
    fill: var(--ink-grey);
    letter-spacing: 0.5px;
  }
  .field-label {
    font-family: "Lato", sans-serif;
    font-size: 26px;
    fill: var(--ink-white);
    letter-spacing: 0.5px;
  }
  .contact-line {
    font-family: "Lato", sans-serif;
    font-size: 15px;
    fill: var(--ink-soft);
    letter-spacing: 0.4px;
  }
</style>
</head>
<body>
<main class="stage">

  <svg class="card card-front" viewBox="0 0 560 320" aria-label="Card front">
    <rect width="560" height="320" fill="var(--card-dark)"/>
    <polygon class="light-field" points="150,0 560,0 560,175 405,320 0,320 0,140"
             fill="var(--light-tint)" role="img" aria-label="Light honeycomb texture field"/>
    <polygon class="accent-block" points="95,60 150,0 205,30 150,92" fill="var(--brand-blue)"/>
    <polygon class="accent-block" points="150,92 205,30 230,44 176,106" fill="var(--brand-blue-soft)"/>
    <polygon class="accent-block" points="440,188 500,120 560,150 560,175 505,225" fill="var(--brand-blue)"/>
    <text class="brand-name" x="280" y="160" font-size="48" text-anchor="middle">CORVALIN</text>
    <text class="site-line" x="280" y="200" text-anchor="middle">www.corvalinbio.com</text>
  </svg>

  <svg class="card card-back" viewBox="0 0 560 320" aria-label="Card back">
    <rect width="560" height="320" fill="var(--card-dark)"/>
    <polygon class="light-field" points="0,0 340,0 205,320 0,320"
             fill="var(--light-tint)" role="img" aria-label="Light honeycomb texture field"/>
    <polygon class="accent-block" points="0,280 160,250 148,280 60,320 0,320" fill="var(--brand-blue)"/>
    <text class="brand-name" x="28" y="150" font-size="38">CORVALIN</text>

    <polygon class="title-band" points="318,52 560,52 560,122 288,122" fill="var(--brand-blue)"/>
    <text class="field-label" x="330" y="93">Biotechnology</text>
    <line x1="330" y1="106" x2="500" y2="106" stroke="var(--ink-white)" stroke-width="1.5"/>
    <line x1="380" y1="110" x2="450" y2="110" stroke="var(--card-dark)" stroke-width="2"/>

    <g class="contact-list">
      <g class="contact-phone">
        <path d="M300 168 q-4 6 2 13 q5 5 9 2 l-3 -4 q-2 1 -4 -1 q-2 -3 0 -5 z" fill="var(--brand-green)"/>
        <text class="contact-line" x="322" y="182">01555014822</text>
      </g>
      <g class="contact-email">
        <rect x="298" y="204" width="16" height="11" fill="var(--brand-green)"/>
        <polyline points="298,204 306,211 314,204" fill="none" stroke="var(--card-dark)" stroke-width="1.2"/>
        <text class="contact-line" x="322" y="215">hello@corvalinbio.com</text>
      </g>
      <g class="contact-web">
        <circle cx="306" cy="243" r="8" fill="var(--brand-green)"/>
        <ellipse cx="306" cy="243" rx="3.5" ry="8" fill="none" stroke="var(--card-dark)" stroke-width="1"/>
        <line x1="298" y1="243" x2="314" y2="243" stroke="var(--card-dark)" stroke-width="1"/>
        <text class="contact-line" x="322" y="248">www.corvalinbio.com</text>
      </g>
    </g>
  </svg>

</main>
</body>
</html>
```